The Marrow Lanterns Podcast

A logo that defines defiance. The "Marrow Lanterns" Podcast with Brent & Quill will revolve around people who have accomplished remarkable things in spite of odds being stacked against them. I want the logo to be simple, marketable, strong and bold, attractive to the eye on a mobile device. The hosts name will be part of the logo. I will give you full creative freedom to the artists to try to create something that is truly legendary and amazing. Please feel free to reach out if you have any questions.Podcast name: The Defying OnesHosts: Brent & Quill
Target Market(s)
Listeners interested in self growth, excitement, inspiration, fun.
Colors
Designer to choose colors to be used in the design.
Look and feel

```html
<!DOCTYPE html>
<html lang="en">
<head>
<meta charset="utf-8">
<title>The Marrow Lanterns — with Brent &amp; Quill</title>
<link href="https://fonts.googleapis.com/css2?family=Marcellus&family=Questrial&display=swap" rel="stylesheet">
<style>
  :root {
    --sky-light: #c4c4c4;
    --sky-mid: #a2a2a2;
    --sky-deep: #8a8a8a;
    --city-dark: #262626;
    --city-mid: #4a4a4a;
    --ink: #2b2b2b;
    --label-box: #2f2f2f;
    --paper: #ffffff;
  }
  html, body {
    margin: 0;
    padding: 0;
    width: 1200px;
    height: 1200px;
    overflow: hidden;
    background: var(--paper);
  }
  .cover {
    position: relative;
    width: 1200px;
    height: 1200px;
    overflow: hidden;
  }
  .skyline-photo {
    position: absolute;
    inset: 0;
  }
  .skyline-photo .sky {
    position: absolute;
    inset: 0;
    background:
      radial-gradient(ellipse 700px 120px at 820px 430px, rgba(230,230,230,0.55), transparent 70%),
      radial-gradient(ellipse 600px 90px at 300px 640px, rgba(225,225,225,0.5), transparent 70%),
      radial-gradient(ellipse 800px 110px at 700px 780px, rgba(110,110,110,0.35), transparent 70%),
      radial-gradient(ellipse 500px 80px at 950px 880px, rgba(215,215,215,0.45), transparent 70%),
      linear-gradient(to bottom, var(--sky-deep) 0%, var(--sky-mid) 30%, var(--sky-light) 50%, var(--sky-mid) 70%, var(--sky-deep) 100%);
  }
  .skyline-photo .city-inverted {
    position: absolute;
    left: 0;
    top: 0;
    width: 1200px;
    height: 330px;
    background:
      radial-gradient(ellipse 140px 320px at 930px 0, rgba(38,38,38,0.85), transparent 75%),
      radial-gradient(ellipse 180px 270px at 520px 0, rgba(38,38,38,0.8), transparent 75%),
      linear-gradient(to bottom, var(--city-dark) 0%, var(--city-dark) 22%, var(--city-mid) 48%, rgba(74,74,74,0.55) 70%, rgba(74,74,74,0) 100%);
  }
  .skyline-photo .city-upright {
    position: absolute;
    left: 0;
    bottom: 0;
    width: 1200px;
    height: 330px;
    background:
      radial-gradient(ellipse 45px 330px at 455px 330px, rgba(50,50,50,0.75), transparent 80%),
      radial-gradient(ellipse 200px 240px at 130px 330px, rgba(40,40,40,0.7), transparent 75%),
      linear-gradient(to top, var(--city-dark) 0%, var(--city-dark) 20%, var(--city-mid) 50%, rgba(74,74,74,0.5) 72%, rgba(74,74,74,0) 100%);
  }
  .slashes {
    position: absolute;
    inset: 0;
  }
  .title {
    position: absolute;
    left: 102px;
    top: 429px;
    margin: 0;
    font-family: "Marcellus", serif;
    font-weight: 400;
    font-size: 86px;
    line-height: 115px;
    letter-spacing: -1px;
    color: var(--ink);
    white-space: nowrap;
  }
  .title-boxed {
    display: inline-block;
    background: var(--label-box);
    color: var(--paper);
    padding-left: 20px;
    height: 115px;
  }
  .hosts {
    position: absolute;
    right: 116px;
    top: 551px;
    margin: 0;
    font-family: "Questrial", sans-serif;
    font-size: 52px;
    line-height: 56px;
    letter-spacing: 0;
    color: var(--ink);
    white-space: nowrap;
  }
</style>
</head>
<body>
  <main class="cover">
    <div class="skyline-photo" role="img" aria-label="Black and white city skyline photo, mirrored upside down along the top and upright along the bottom, with a streaky cloudy grey sky between">
      <div class="sky"></div>
      <div class="city-inverted"></div>
      <div class="city-upright"></div>
    </div>

    <svg class="slashes" width="1200" height="1200" viewBox="0 0 1200 1200" aria-hidden="true">
      <line x1="176" y1="0" x2="0" y2="677" stroke="#ffffff" stroke-width="6"/>
      <line x1="1200" y1="677" x2="1076" y2="1200" stroke="#ffffff" stroke-width="6"/>
      <line x1="615" y1="328" x2="545" y2="615" stroke="#ffffff" stroke-width="2.5"/>
    </svg>

    <h1 class="title"><span class="title-boxed">THE MARR</span>OW LANTERNS</h1>
    <p class="hosts">WITH BRENT &amp; QUILL</p>
  </main>
</body>
</html>
```